"Corporate Site Design of Cloud Application Venture"(Wordpress Design Project)

This task is new corporate site design for start-up.
Our company name is "Vantreel."
Vantreel is a cloud service for users who want to bring their software and settings on multiple computers.
Current beta service page is http://demo.vantreel-example.com . But, now it is not available.
We suggest sample sites below. But, we don't want to follow there. We need you to focus our logo and our company will serve stable service.
http://www.gallopix-example.com/design/481203/site-design-by-nortfield
http://www.gallopix-example.com/design/492715/site-design-by-qm
http://www.gallopix-example.com/design/470392
http://www.gallopix-example.com/design/418857
http://www.gallopix-example.com/design/409136
http://www.gallopix-example.com/design/413278
http://www.kintrabo-example.com/portfolio/plumvane/
http://tesselmarket-example.net/item/design-company-site/27415
http://www.orlivetstudio-example.com/images/corporate-dl-thumb.jpg
http://www.quorvenmart-example.com/product-tp/562093814/web_site_design_company.html
(1)we have already had logo-design and please must use it (attached).
we have attached 2 files.
Essential : vantreel.ai
voluntary : vantreelicon.ai
(2)Unfortunately, we have no idea now, so depend on you about color, lay-out and something, but we wish people feel deeply impressive when they get our website.
(3)Only if you want to use phrase of my service, please use “Where there is Vantreel, there’s your workspace.” (if the English grammar is not correct, please modify it.)
(4)The final design should look modern and sophisticated.
(5)Must have these contents.
In header.
- logo and facebook page link.(http://www.plinkhub-example.com/vantreel)
In Header Menu.
- Top Page (has several news release)
- "News Release" List and News Release Page
- "About Service"
- "About Us"
- "Contact"
And footter has several links.
ex. News release, about service, about us, contact, hiring and so on.

```html
<!DOCTYPE html>
<html lang="en">
<head>
<meta charset="utf-8">
<title>Vantreel — Where there is Vantreel, there's your workspace</title>
<link href="https://fonts.googleapis.com/css2?family=Mulish:wght@300;400;600&family=Arimo:wght@400;700&display=swap" rel="stylesheet">
<style>
  :root{
    --bg:#f3f2ef;
    --header:#2d2d2d;
    --header-line:#3c3c3c;
    --nav-active:#d9dcdf;
    --text-soft:#8a8f98;
    --text-body:#8c8c8c;
    --heading:#5d6a78;
    --dark:#353535;
    --green:#3fae2a;
    --yellow:#f4c752;
    --pink:#fb6592;
    --orange:#fb9358;
    --panel:#ffffff;
    --panel-grey:#eeeeee;
    --rule:#e2e2e2;
    --arrow:#c6c9cd;
    --scene-top:#b9d98c;
    --scene-bottom:#6fa9c9;
  }
  *{box-sizing:border-box;margin:0;padding:0}
  html,body{width:1087px;height:1200px;overflow:hidden}
  body{background:var(--bg);font-family:"Arimo",Arial,sans-serif;color:var(--text-body);position:relative}

  /* header */
  .site-header{position:absolute;left:0;top:0;width:1087px;height:67px;background:var(--header);border-bottom:2px solid #1e1e1e}
  .brand{position:absolute;left:163px;top:13px;display:flex;align-items:center;gap:12px;color:#fff;font-family:"Mulish",sans-serif;font-weight:400;font-size:34px;letter-spacing:.5px}
  .brand-dot{width:30px;height:30px;border-radius:50%;background:#fff}
  .main-nav{position:absolute;left:452px;top:0;height:67px;display:flex}
  .main-nav a{display:block;height:67px;line-height:67px;padding:0 16px;color:#e9e9e9;font-family:"Mulish",sans-serif;font-size:14px;text-decoration:none;border-left:1px solid var(--header-line)}
  .main-nav a:last-child{border-right:1px solid var(--header-line)}
  .main-nav a.is-active{background:var(--nav-active);color:#555}

  .social{position:absolute;left:870px;top:81px;display:flex;gap:3px}
  .social span{width:15px;height:15px;background:#3b6fb3;display:block}

  /* hero */
  .slider-arrow{position:absolute;width:37px;height:37px;border-radius:50%;background:var(--arrow)}
  .slider-arrow svg{position:absolute;left:0;top:0}
  .tagline{position:absolute;left:149px;font-family:"Mulish",sans-serif;font-weight:300;font-size:23px;color:var(--text-soft);background:#fff;padding:0 14px;height:46px;line-height:46px;box-shadow:0 1px 3px rgba(0,0,0,.15)}
  .btn-download{position:absolute;left:148px;top:295px;width:250px;height:71px;background:var(--dark);color:#fff;font-family:"Mulish",sans-serif;font-weight:300;font-size:33px;padding-left:16px;line-height:71px;box-shadow:0 2px 4px rgba(0,0,0,.3)}
  .btn-download svg{position:absolute;right:22px;top:14px}
  .hero-device{position:absolute;left:551px;top:121px;width:381px;height:329px;border-radius:6px;background:linear-gradient(160deg,#2a2a2e 0%,#4b1e5e 40%,#c04aa9 55%,#2a1540 75%,#9a9a9e 100%)}

  /* feature tiles */
  .tile{position:absolute;color:#fff;font-family:"Mulish",sans-serif;font-size:16px;text-align:center}
  .tile svg{display:block;margin:0 auto}
  .tile-apps{left:148px;top:477px;width:264px;height:160px;background:var(--yellow);color:#5a4a20;padding-top:24px}
  .tile-config{left:412px;top:467px;width:264px;height:178px;background:var(--pink);padding-top:32px;z-index:2;box-shadow:0 2px 6px rgba(0,0,0,.12)}
  .tile-share{left:676px;top:477px;width:264px;height:160px;background:var(--orange);padding-top:24px}
  .tile p{margin-top:14px}

  /* content panel */
  .content-panel{position:absolute;left:148px;top:680px;width:807px;height:264px;background:var(--panel)}
  .col-title{font-family:"Mulish",sans-serif;font-weight:400;font-size:17px;color:var(--heading)}
  .welcome{position:absolute;left:23px;top:30px;width:218px}
  .welcome .col-title{display:flex;align-items:center;gap:8px}
  .welcome .col-title i{width:18px;height:18px;border-radius:50%;background:var(--heading);display:block}
  .welcome p{font-size:10px;line-height:13.5px;margin-top:10px;text-align:justify}
  .services{position:absolute;left:253px;top:30px;width:205px}
  .service-item{display:flex;gap:10px;align-items:flex-start;border-bottom:1px solid var(--rule);padding:10px 0 8px;font-size:10px;line-height:12.5px}
  .service-item:last-child{border-bottom:0}
  .service-item svg{flex:0 0 22px}
  .testimonials{position:absolute;left:483px;top:23px;width:307px;height:207px;background:var(--panel-grey)}
  .testimonials .col-title{position:absolute;left:28px;top:12px}
  .mini-arrows{position:absolute;right:14px;top:14px;display:flex;gap:4px}
  .mini-arrows span{width:16px;height:16px;border-radius:50%;background:var(--arrow);display:block}
  .quote-mark{position:absolute;font-family:Georgia,serif;font-size:60px;color:#dcdcdc;line-height:1}
  .avatar{position:absolute;left:38px;top:64px;width:72px;height:72px;border-radius:50%;background:radial-gradient(circle,#c9a07f 0%,#e6d7c8 60%,#fff 70%);border:3px solid #fff;box-shadow:0 0 0 1px #ddd}
  .testimonials blockquote{position:absolute;left:118px;top:64px;width:160px;font-size:10px;line-height:13.5px}
  .testimonials cite{position:absolute;right:46px;top:144px;font-style:normal;font-weight:700;font-size:11px;color:#6b7480}

  /* footer */
  .footer-col{position:absolute;top:975px}
  .footer-col h3{font-family:"Mulish",sans-serif;font-weight:400;font-size:16px;color:var(--heading)}
  .sitemap{left:157px}
  .sitemap ul{list-style:none;margin-top:8px}
  .sitemap li{font-size:10px;line-height:19px;display:flex;align-items:center;gap:8px}
  .sitemap li::before{content:"";width:6px;height:6px;background:#9aa0a8;display:block}
  .news{left:343px;width:254px}
  .news strong{display:block;font-size:10px;color:#555;margin-top:10px}
  .news p{font-size:10px;line-height:12px;margin-top:3px}
  .news-arrow{position:absolute;width:17px;height:17px;border-radius:50%;background:var(--arrow);top:1026px}
  .newsletter{left:683px;width:260px}
  .newsletter .hint{font-size:10px;margin-top:2px}
  .subscribe{display:flex;margin-top:15px}
  .subscribe span{width:223px;height:28px;background:#fff;border:1px solid #e0e0e0;font-size:10px;font-style:italic;color:#bbb;line-height:26px;padding-left:12px}
  .subscribe b{width:29px;height:28px;background:#3a3a3a;color:#fff;font-size:12px;font-weight:400;text-align:center;line-height:28px}
  .newsletter .copy{font-size:10px;margin-top:10px}

  .footer-scene{position:absolute;left:140px;top:1120px;width:807px;height:80px;background:linear-gradient(180deg,var(--scene-top) 0%,var(--scene-bottom) 100%)}
</style>
</head>
<body>

<header class="site-header">
  <div class="brand"><span class="brand-dot"></span>Vantreel</div>
  <nav class="main-nav">
    <a class="is-active" href="#">Home</a>
    <a href="#">About Us</a>
    <a href="#">News Release</a>
    <a href="#">About Service</a>
    <a href="#">Contact Us</a>
  </nav>
</header>

<div class="social" aria-label="Social links"><span></span><span></span><span></span></div>

<section class="hero">
  <div class="slider-arrow" style="left:69px;top:238px">
    <svg width="37" height="37"><path d="M21 11 L14 18.5 L21 26" stroke="#fff" stroke-width="3.5" fill="none" stroke-linecap="round"/></svg>
  </div>
  <div class="slider-arrow" style="left:973px;top:238px">
    <svg width="37" height="37"><path d="M16 11 L23 18.5 L16 26" stroke="#fff" stroke-width="3.5" fill="none" stroke-linecap="round"/></svg>
  </div>
  <div class="tagline" style="top:174px">Where there is Vantreel,there's</div>
  <div class="tagline" style="top:221px">your workspace!</div>
  <a class="btn-download">Download
    <svg width="38" height="42" viewBox="0 0 38 42"><path d="M12 0h14v14h9L19 31 3 14h9z" fill="var(--green)"/><rect x="3" y="34" width="32" height="7" fill="var(--green)"/></svg>
  </a>
  <div class="hero-device" role="img" aria-label="Desktop monitor showing the Vantreel start screen"></div>
</section>

<section class="features">
  <div class="tile tile-apps">
    <svg width="78" height="78" viewBox="0 0 78 78" fill="none" stroke="#fff" stroke-width="4"><circle cx="39" cy="39" r="34"/><ellipse cx="39" cy="39" rx="15" ry="34"/><line x1="39" y1="5" x2="39" y2="73"/><line x1="5" y1="39" x2="73" y2="39"/><path d="M11 22h56M11 56h56"/></svg>
    <p>Bring your apps anywhere</p>
  </div>
  <div class="tile tile-config">
    <svg width="84" height="84" viewBox="0 0 84 84"><g fill="#fff"><circle cx="42" cy="42" r="31"/><rect x="38" y="2" width="8" height="12"/><rect x="38" y="70" width="8" height="12"/><rect x="2" y="38" width="12" height="8"/><rect x="70" y="38" width="12" height="8"/><g transform="rotate(45 42 42)"><rect x="38" y="2" width="8" height="12"/><rect x="38" y="70" width="8" height="12"/><rect x="2" y="38" width="12" height="8"/><rect x="70" y="38" width="12" height="8"/></g></g><g fill="var(--pink)"><circle cx="42" cy="42" r="6"/><circle cx="42" cy="25" r="6"/><circle cx="42" cy="59" r="6"/><circle cx="25" cy="42" r="6"/><circle cx="59" cy="42" r="6"/></g></svg>
    <p>Bring your configue anywhere</p>
  </div>
  <div class="tile tile-share">
    <svg width="100" height="78" viewBox="0 0 100 78" fill="none" stroke="#fff" stroke-width="8"><circle cx="50" cy="39" r="20"/><line x1="4" y1="39" x2="28" y2="39"/><line x1="72" y1="39" x2="96" y2="39"/></svg>
    <p>Share your apps with friends</p>
  </div>
</section>

<section class="content-panel">
  <div class="welcome">
    <h2 class="col-title"><i></i>Welcome to Vantreel</h2>
    <p>We can not tell you exactly when we will be sending out the invitations, but we promise to open our evice to those registered with priority. Lorem Ipsum is simply dummy text of the printing and typesetting industry. Lorem Ipsum has been the industry's standard dummy text ever since the 1500s, when an unknown printer took.</p>
    <p>Galley of type and scrambled it to make a type specimen book.</p>
  </div>
  <div class="services">
    <h2 class="col-title">Vantreel Services</h2>
    <div class="service-item"><svg width="22" height="22" fill="none" stroke="#6b7480" stroke-width="2"><circle cx="11" cy="11" r="9"/><circle cx="11" cy="11" r="4"/></svg><span>We can not tell you exactly when we will be sending out the invitations.</span></div>
    <div class="service-item"><svg width="22" height="22" fill="#6b7480"><circle cx="11" cy="11" r="7"/><rect x="9" y="1" width="4" height="20"/><rect x="1" y="9" width="20" height="4"/><circle cx="11" cy="11" r="3" fill="#fff"/></svg><span>We can not tell you exactly when we will be sending out the invitations.</span></div>
    <div class="service-item"><svg width="22" height="22" fill="#6b7480"><rect x="2" y="7" width="18" height="12" rx="1"/><rect x="8" y="4" width="6" height="4" fill="none" stroke="#6b7480" stroke-width="1.5"/><rect x="2" y="11" width="18" height="1.5" fill="#fff"/></svg><span>Tell you exactly when we will be sending out the invitations.</span></div>
    <div class="service-item"><svg width="22" height="22" fill="none" stroke="#6b7480" stroke-width="2.5" stroke-linecap="round"><path d="M4 18l5-5M13 9l5-5M8 14l6-6"/></svg><span>We can not tell you exactly when we will be sending out the invitations.</span></div>
  </div>
  <aside class="testimonials">
    <h2 class="col-title">Testimonials</h2>
    <div class="mini-arrows"><span></span><span></span></div>
    <span class="quote-mark" style="left:18px;top:46px">“</span>
    <div class="avatar" role="img" aria-label="Customer portrait"></div>
    <blockquote>We can not tell you exactly when we will be sending out the invitations, but we promise to open our evice to those registered with priority.</blockquote>
    <cite>Ravel Dunmore</cite>
    <span class="quote-mark" style="left:262px;top:136px">”</span>
  </aside>
</section>

<footer>
  <div class="footer-col sitemap">
    <h3>Site Map</h3>
    <ul><li>News Release</li><li>About Service</li><li>About Us</li><li>Contact Us</li></ul>
  </div>
  <span class="news-arrow" style="left:312px"></span>
  <div class="footer-col news">
    <h3>News</h3>
    <strong>We can not tell you exactly when we will be sending</strong>
    <p>We can not tell you exactly when we will be sending out the invitations, but we promise to open our evice to those registered with priority.</p>
  </div>
  <span class="news-arrow" style="left:607px"></span>
  <div class="footer-col newsletter">
    <h3>Subscribe Newsletter</h3>
    <p class="hint">Dummy text can not tell you exactly when we will.</p>
    <div class="subscribe"><span>email adress</span><b>Go</b></div>
    <p class="copy">© 2012Vantreel.com. designed by Quillnest Studio.</p>
  </div>
</footer>

<div class="footer-scene" role="img" aria-label="Illustration of a small planet with sea, hills, houses and city buildings"></div>

</body>
</html>
```